Banner Graphics For Quillo Storefront Page

Hello,
I am looking for a designer to help me with a banner heading that I want to place on my Quillo storefront page. My company sells outdoor kitchen/bbq island accessories. I would like for it to have a background photo with text/logo & graphics overlaid on the image. If possible I would like it to include the 5 small "benefit boxes" that are attached on the file that features graphics for one of the products that I sell . I have also included a color photo of my products in actual use. Feel free to use it but if you have a better idea of a background image feel free to try it, maybe a lifestyle stock photo?? Or maybe something else?? I am open to all ideas and you are the creative ones:) Feel free to be creative. The pixel requirements for final image is 3,000 pixels by 600 pixels. Let me know if you have any questions. THANKS! P.s. I also included some stock photos that I like to give you some ideas.

```html
<!DOCTYPE html>
<html lang="en">
<head>
<meta charset="utf-8">
<title>Crestline Storefront Banner Concepts</title>
<link rel="stylesheet" href="https://fonts.googleapis.com/css2?family=PT+Serif:wght@400;700&family=Open+Sans:wght@300;400;700;800&display=swap">
<style>
  :root {
    --stage-light: #eaf4fb;
    --stage-edge: #c9e2f2;
    --ink-white: #ffffff;
    --badge-grey: #8d8d8d;
    --badge-dark: #2b2b2b;
    --badge-mark: #b9b9b9;
    --photo-dark: #2a2622;
    --photo-mid: #4a3f35;
    --photo-warm: #6b4a33;
  }
  * { box-sizing: border-box; margin: 0; padding: 0; }
  html, body { width: 1200px; height: 1200px; overflow: hidden; }
  body {
    background: radial-gradient(ellipse at center, var(--stage-light) 0%, #d9ebf6 60%, var(--stage-edge) 100%);
    position: relative;
    font-family: "Open Sans", sans-serif;
  }
  .banner {
    position: absolute;
    left: 84px;
    width: 1031px;
    height: 206px;
    overflow: hidden;
    box-shadow: 0 8px 22px rgba(40, 70, 100, 0.35);
  }
  .banner--one { top: 180px; }
  .banner--two { top: 486px; }
  .banner--three { top: 791px; }

  .banner__photo { position: absolute; inset: 0; }
  .photo--feast {
    background:
      radial-gradient(circle at 25% 40%, rgba(120, 70, 40, 0.55), transparent 35%),
      radial-gradient(circle at 60% 55%, rgba(90, 110, 70, 0.45), transparent 30%),
      radial-gradient(circle at 85% 35%, rgba(140, 100, 70, 0.45), transparent 35%),
      linear-gradient(90deg, var(--photo-dark), var(--photo-mid) 50%, var(--photo-dark));
  }
  .photo--feast-glow {
    background:
      linear-gradient(160deg, transparent 40%, rgba(58, 123, 213, 0) 70%, rgba(58, 123, 213, 0.55) 100%),
      linear-gradient(200deg, rgba(58, 123, 213, 0.5) 0%, transparent 22%),
      radial-gradient(circle at 25% 40%, rgba(100, 70, 50, 0.5), transparent 35%),
      radial-gradient(circle at 60% 55%, rgba(80, 100, 80, 0.45), transparent 30%),
      linear-gradient(90deg, #20242a, #3c3a38 50%, #22262c);
  }
  .photo--friends {
    background:
      radial-gradient(circle at 30% 40%, rgba(170, 120, 80, 0.55), transparent 35%),
      radial-gradient(circle at 55% 20%, rgba(150, 150, 90, 0.5), transparent 40%),
      radial-gradient(circle at 85% 50%, rgba(120, 80, 60, 0.5), transparent 35%),
      linear-gradient(90deg, #2e2620, var(--photo-warm) 45%, #4a3a2c 75%, #2a231d);
  }

  .brand {
    position: absolute;
    left: 60px;
    top: 80px;
    width: 158px;
    color: var(--ink-white);
    text-align: center;
  }
  .brand__name {
    font-family: "PT Serif", serif;
    font-weight: 400;
    font-size: 30px;
    line-height: 1;
    letter-spacing: 0.5px;
  }
  .brand__tagline {
    font-family: "PT Serif", serif;
    font-size: 12px;
    letter-spacing: 2.6px;
    margin-top: 10px;
    white-space: nowrap;
  }

  .headline {
    position: absolute;
    left: 300px;
    width: 380px;
    top: 74px;
    text-align: center;
    color: var(--ink-white);
    line-height: 1.22;
  }
  .headline--serif { font-family: "PT Serif", serif; font-size: 27px; }
  .headline--serif .headline__light { font-weight: 400; }
  .headline--serif .headline__bold { font-weight: 700; }
  .headline--sans { font-family: "Open Sans", sans-serif; font-size: 24px; top: 76px; left: 297px; }
  .headline--sans .headline__light { font-weight: 300; }
  .headline--sans .headline__bold { font-weight: 700; }

  .benefits {
    position: absolute;
    left: 714px;
    top: 66px;
    display: flex;
    gap: 4px;
  }
  .benefit {
    width: 52px;
    height: 88px;
    border: 1.5px solid var(--ink-white);
    border-radius: 4px;
    overflow: hidden;
    display: flex;
    flex-direction: column;
  }
  .benefit__icon {
    height: 40px;
    background: var(--ink-white);
    display: flex;
    align-items: center;
    justify-content: center;
  }
  .benefit__mark {
    width: 30px;
    height: 30px;
    background: var(--badge-mark);
  }
  .benefit__mark--round { border-radius: 50%; }
  .benefit__label {
    background: var(--badge-grey);
    color: var(--ink-white);
    font-size: 5.5px;
    font-weight: 700;
    text-align: center;
    line-height: 1.05;
    height: 14px;
    display: flex;
    align-items: center;
    justify-content: center;
  }
  .benefit__note {
    flex: 1;
    background: var(--badge-dark);
    color: var(--ink-white);
    font-size: 4.3px;
    text-align: center;
    line-height: 1.2;
    padding: 4px 3px 0;
  }
</style>
</head>
<body>

  <section class="banner banner--one">
    <div class="banner__photo photo--feast" role="img" aria-label="Overhead photo of a wooden table laden with grilled dishes, salads and shared plates"></div>
    <div class="brand">
      <div class="brand__name">CRESTLINE</div>
      <div class="brand__tagline">outdoor kitchens</div>
    </div>
    <h1 class="headline headline--serif">
      <span class="headline__light">outdoor</span> <span class="headline__bold">kitchen/</span><br>
      <span class="headline__light">bbq island</span> <span class="headline__bold">accessories</span>
    </h1>
    <div class="benefits">
      <div class="benefit">
        <div class="benefit__icon"><div class="benefit__mark benefit__mark--round" role="img" aria-label="Handcrafted quality badge"></div></div>
        <div class="benefit__label">QUALITY</div>
        <div class="benefit__note">Our employees take Pride in their Work</div>
      </div>
      <div class="benefit">
        <div class="benefit__icon"><div class="benefit__mark" role="img" aria-label="Double wall construction badge"></div></div>
        <div class="benefit__label">VALUE</div>
        <div class="benefit__note">Our doors weigh 10 Pounds More than the competition</div>
      </div>
      <div class="benefit">
        <div class="benefit__icon"><div class="benefit__mark" role="img" aria-label="Premium stainless steel grade badge"></div></div>
        <div class="benefit__label">STRENGTH</div>
        <div class="benefit__note">Offers higher level of Corrosion Resistance</div>
      </div>
      <div class="benefit">
        <div class="benefit__icon"><div class="benefit__mark" role="img" aria-label="Steel gauge thickness badge"></div></div>
        <div class="benefit__label">DURABILITY</div>
        <div class="benefit__note">Thick and Durable Stainless Steel Construction</div>
      </div>
      <div class="benefit">
        <div class="benefit__icon"><div class="benefit__mark benefit__mark--round" role="img" aria-label="Satisfaction guarantee badge"></div></div>
        <div class="benefit__label">PEACE<br>OF MIND</div>
        <div class="benefit__note">Your Satisfaction is our highest priority</div>
      </div>
    </div>
  </section>

  <section class="banner banner--two">
    <div class="banner__photo photo--feast-glow" role="img" aria-label="Overhead photo of a shared barbecue feast on a wooden table with streaks of blue light"></div>
    <div class="brand">
      <div class="brand__name">CRESTLINE</div>
      <div class="brand__tagline">outdoor kitchens</div>
    </div>
    <h1 class="headline headline--sans">
      <span class="headline__light">outdoor</span> <span class="headline__bold">kitchen/</span><br>
      <span class="headline__light">bbq</span> <span class="headline__bold">island accessories</span>
    </h1>
    <div class="benefits">
      <div class="benefit">
        <div class="benefit__icon"><div class="benefit__mark benefit__mark--round" role="img" aria-label="Handcrafted quality badge"></div></div>
        <div class="benefit__label">QUALITY</div>
        <div class="benefit__note">Our employees take Pride in their Work</div>
      </div>
      <div class="benefit">
        <div class="benefit__icon"><div class="benefit__mark" role="img" aria-label="Double wall construction badge"></div></div>
        <div class="benefit__label">VALUE</div>
        <div class="benefit__note">Our doors weigh 10 Pounds More than the competition</div>
      </div>
      <div class="benefit">
        <div class="benefit__icon"><div class="benefit__mark" role="img" aria-label="Premium stainless steel grade badge"></div></div>
        <div class="benefit__label">STRENGTH</div>
        <div class="benefit__note">Offers higher level of Corrosion Resistance</div>
      </div>
      <div class="benefit">
        <div class="benefit__icon"><div class="benefit__mark" role="img" aria-label="Steel gauge thickness badge"></div></div>
        <div class="benefit__label">DURABILITY</div>
        <div class="benefit__note">Thick and Durable Stainless Steel Construction</div>
      </div>
      <div class="benefit">
        <div class="benefit__icon"><div class="benefit__mark benefit__mark--round" role="img" aria-label="Satisfaction guarantee badge"></div></div>
        <div class="benefit__label">PEACE<br>OF MIND</div>
        <div class="benefit__note">Your Satisfaction is our highest priority</div>
      </div>
    </div>
  </section>

  <section class="banner banner--three">
    <div class="banner__photo photo--friends" role="img" aria-label="Lifestyle photo of friends sharing food and drinks at an outdoor table in warm sunlight"></div>
    <div class="brand">
      <div class="brand__name">CRESTLINE</div>
      <div class="brand__tagline">outdoor kitchens</div>
    </div>
    <h1 class="headline headline--sans">
      <span class="headline__light">outdoor</span> <span class="headline__bold">kitchen/</span><br>
      <span class="headline__light">bbq</span> <span class="headline__bold">island accessories</span>
    </h1>
    <div class="benefits">
      <div class="benefit">
        <div class="benefit__icon"><div class="benefit__mark benefit__mark--round" role="img" aria-label="Handcrafted quality badge"></div></div>
        <div class="benefit__label">QUALITY</div>
        <div class="benefit__note">Our employees take Pride in their Work</div>
      </div>
      <div class="benefit">
        <div class="benefit__icon"><div class="benefit__mark" role="img" aria-label="Double wall construction badge"></div></div>
        <div class="benefit__label">VALUE</div>
        <div class="benefit__note">Our doors weigh 10 Pounds More than the competition</div>
      </div>
      <div class="benefit">
        <div class="benefit__icon"><div class="benefit__mark" role="img" aria-label="Premium stainless steel grade badge"></div></div>
        <div class="benefit__label">STRENGTH</div>
        <div class="benefit__note">Offers higher level of Corrosion Resistance</div>
      </div>
      <div class="benefit">
        <div class="benefit__icon"><div class="benefit__mark" role="img" aria-label="Steel gauge thickness badge"></div></div>
        <div class="benefit__label">DURABILITY</div>
        <div class="benefit__note">Thick and Durable Stainless Steel Construction</div>
      </div>
      <div class="benefit">
        <div class="benefit__icon"><div class="benefit__mark benefit__mark--round" role="img" aria-label="Satisfaction guarantee badge"></div></div>
        <div class="benefit__label">PEACE<br>OF MIND</div>
        <div class="benefit__note">Your Satisfaction is our highest priority</div>
      </div>
    </div>
  </section>

</body>
</html>
```